Dr. Marissa Tevlin Medical/Chiropractic Business Card

Dr. Tevlin is a chiropractor and will require a business card that she uses every single day to book appointments on the back side of the card. Currently the office name goes by Dr. Marissa Tevlin. The chiropractic profession is based on the diagnosis and manipulative treatment of misalignments of the joints, especially those of the spinal column, which are held to cause other disorders by affecting the nerves, muscles, and organs. Dr. Marissa Tevlin is looking for a contemporary and minimalistic design.

Industry/Entity Type

Medical

Contact Information for Business Card

Name: Dr. Marissa Tevlin; Address: 748 Harcastle Rd South, London, ON N5R 2K7; Phone Number: 519.274.6193; Fax: 519.281.5046; email: marissa.tevlin@quorvamail.com

Requirements
Must have
• ability to write multiple appointments date/time on the back of card

```html
<!DOCTYPE html>
<html lang="en">
<head>
<meta charset="utf-8">
<title>Dr. Marissa Tevlin – Business Card</title>
<link href="https://fonts.googleapis.com/css2?family=Noticia+Text:wght@400;700&display=swap" rel="stylesheet">
<style>
  :root {
    --bg: #e8e5e1;
    --card: #ffffff;
    --card-edge: #2b2b2b;
    --accent-red: #d42a1f;
    --rule-red: #c94a42;
    --ink: #2a2a2a;
    --ink-soft: #555555;
    --line: #3a3a3a;
  }
  * { margin: 0; padding: 0; box-sizing: border-box; }
  html, body { width: 1200px; height: 1000px; overflow: hidden; }
  body {
    background: var(--bg);
    font-family: "Noticia Text", Georgia, serif;
    color: var(--ink);
    position: relative;
  }
  .card {
    position: absolute;
    top: 183px;
    width: 359px;
    height: 612px;
    background: var(--card);
    border: 1.5px solid var(--card-edge);
    border-radius: 14px;
    box-shadow: 0 4px 10px rgba(0,0,0,0.25);
  }
  .card--front { left: 237px; }
  .card--back { left: 626px; }

  .centered { position: absolute; left: 0; width: 100%; text-align: center; }

  .doctor-name {
    top: 205px;
    font-size: 27px;
    font-weight: 700;
    color: var(--accent-red);
    letter-spacing: 0.5px;
    font-variant: small-caps;
  }
  .profession {
    top: 238px;
    font-size: 25px;
    color: var(--ink-soft);
    letter-spacing: 0.3px;
  }
  .divider {
    position: absolute;
    top: 437px;
    left: 35px;
    width: 289px;
    height: 1.5px;
    background: var(--rule-red);
  }
  .contact {
    top: 469px;
    font-size: 15.5px;
    line-height: 21px;
  }
  .address {
    top: 546px;
    font-size: 15.5px;
    line-height: 21px;
  }

  .patient-label { top: 16px; font-size: 17px; color: var(--ink-soft); }
  .name-line {
    position: absolute; top: 74px; left: 21px; width: 315px; height: 1.5px; background: var(--line);
  }
  .appointments-title {
    top: 98px; font-size: 18px; color: var(--ink-soft); text-decoration: underline; text-underline-offset: 3px;
  }
  .col-head {
    position: absolute; top: 137px; font-size: 16px; color: var(--ink-soft);
    text-decoration: underline; text-underline-offset: 3px;
  }
  .col-head--date { left: 70px; }
  .col-head--time { left: 247px; }
  .entry-lines { position: absolute; top: 0; left: 0; }
  .reschedule-note {
    top: 550px; font-size: 13.5px; line-height: 18px; color: var(--ink-soft);
  }
</style>
</head>
<body>
  <section class="card card--front" aria-label="Card front">
    <h1 class="centered doctor-name">Dr. Marissa Tevlin</h1>
    <p class="centered profession">Chiropractor</p>
    <div class="divider"></div>
    <p class="centered contact">P: 519.274.6193<br>F: 519.281.5046<br>E: marissa.tevlin@quorvamail.com</p>
    <p class="centered address">748 Harcastle Rd South<br>London, ON N5R 2K7</p>
  </section>

  <section class="card card--back" aria-label="Card back">
    <p class="centered patient-label">Patient’s Name</p>
    <div class="name-line"></div>
    <p class="centered appointments-title">Appointments</p>
    <span class="col-head col-head--date">Date</span>
    <span class="col-head col-head--time">Time</span>
    <svg class="entry-lines" width="359" height="612" viewBox="0 0 359 612" aria-hidden="true">
      <g stroke="#3a3a3a" stroke-width="1.2">
        <line x1="21" y1="194" x2="157" y2="194"/><line x1="199" y1="194" x2="335" y2="194"/>
        <line x1="21" y1="232" x2="157" y2="232"/><line x1="199" y1="232" x2="335" y2="232"/>
        <line x1="21" y1="270" x2="157" y2="270"/><line x1="199" y1="270" x2="335" y2="270"/>
        <line x1="21" y1="308" x2="157" y2="308"/><line x1="199" y1="308" x2="335" y2="308"/>
        <line x1="21" y1="346" x2="157" y2="346"/><line x1="199" y1="346" x2="335" y2="346"/>
        <line x1="21" y1="384" x2="157" y2="384"/><line x1="199" y1="384" x2="335" y2="384"/>
        <line x1="21" y1="422" x2="157" y2="422"/><line x1="199" y1="422" x2="335" y2="422"/>
        <line x1="21" y1="460" x2="157" y2="460"/><line x1="199" y1="460" x2="335" y2="460"/>
        <line x1="21" y1="498" x2="157" y2="498"/><line x1="199" y1="498" x2="335" y2="498"/>
        <line x1="21" y1="536" x2="157" y2="536"/><line x1="199" y1="536" x2="335" y2="536"/>
      </g>
    </svg>
    <p class="centered reschedule-note">If you are unable to make your appointment,<br>please call us to reschedule.</p>
  </section>
</body>
</html>
```